Business Card Design

Our Motto is "Protecting Australia's Underground Utilities"

We want the Southern Cross inside a shield I have attached the southern cross and our old shield design

Product description is: Vacuum Excavation & Utility Location
Wet & Dry Vacuum Loading
Confined Space Entry Specialists
High Pressure Cleaning

The Southern Cross in the shield must be blue and white. The Company name must be Coastal Pipeguard Services. The Green & Gold Shield logo I uploaded is my OLD logo design. Thank you

Target Market(s)

Civil Construction

Industry/Entity Type

Business

Contact Information for Business Card

Coastal Pipeguard Services Pty Ltd
Corey Halbrook(Director)
0413862975
coreyh@pipeguardco.com.au
A.B.N.52938470116

Colors
0456a3

Requirements
Must have
• Southern Cross inside a shield, Blue and white design on the Southern Cross shield.
Must say Coastal Pipeguard Services P/L

```html
<!DOCTYPE html>
<html lang="en">
<head>
<meta charset="utf-8">
<title>Coastal Pipeguard Services P/L – Business Card</title>
<link href="https://fonts.googleapis.com/css2?family=Questrial&display=swap" rel="stylesheet">
<style>
  :root {
    --frame-black: #000000;
    --paper-white: #ffffff;
    --brand-blue: #1530d8;
    --brand-navy: #0456a3;
    --text-white: #ffffff;
    --icon-blue: #1f6fe8;
  }
  html, body {
    margin: 0;
    padding: 0;
    width: 1200px;
    height: 742px;
    overflow: hidden;
    background: var(--paper-white);
  }
  .card {
    position: relative;
    width: 1200px;
    height: 742px;
    box-sizing: border-box;
    border: 4px solid var(--frame-black);
    background: var(--paper-white);
    font-family: "Questrial", "Arial", sans-serif;
  }
  .card__face {
    position: absolute;
    left: 16px;
    top: 16px;
    width: 1160px;
    height: 702px;
    box-sizing: border-box;
    border: 2px solid var(--frame-black);
    overflow: hidden;
  }
  .card__backdrop {
    position: absolute;
    inset: 0;
    width: 100%;
    height: 100%;
  }
  .brand-mark {
    position: absolute;
    left: 497px;
    top: 18px;
    width: 160px;
    height: 160px;
    border-radius: 50%;
    background: var(--brand-blue);
  }
  .company-name {
    position: absolute;
    left: 0;
    right: 0;
    top: 222px;
    margin: 0;
    text-align: center;
    color: var(--brand-blue);
    font-size: 26px;
    font-weight: 400;
    line-height: 24.5px;
    letter-spacing: 6px;
    text-transform: uppercase;
  }
  .company-name span { display: block; }
  .motto {
    position: absolute;
    left: 56px;
    right: 0;
    top: 316px;
    margin: 0;
    text-align: center;
    color: var(--text-white);
    font-size: 44px;
    line-height: 50px;
    letter-spacing: 4.5px;
    white-space: nowrap;
  }
  .services {
    position: absolute;
    left: 130px;
    top: 402px;
    margin: 0;
    padding: 0;
    list-style: none;
  }
  .services__item {
    display: flex;
    align-items: center;
    height: 54px;
    color: var(--brand-blue);
    font-size: 46px;
    letter-spacing: 4.5px;
    white-space: nowrap;
  }
  .services__star {
    width: 38px;
    height: 38px;
    margin-right: 20px;
    fill: var(--text-white);
  }
  .contact {
    position: absolute;
    top: 646px;
    display: flex;
    align-items: center;
    color: var(--text-white);
    font-size: 32px;
    letter-spacing: 5px;
    white-space: nowrap;
  }
  .contact--email { left: 12px; }
  .contact--phone { left: 739px; letter-spacing: 10px; }
  .contact__icon {
    width: 54px;
    height: 54px;
    margin-right: 24px;
  }
</style>
</head>
<body>
<div class="card">
  <div class="card__face">
    <svg class="card__backdrop" viewBox="0 0 1160 702" preserveAspectRatio="none" aria-hidden="true">
      <defs>
        <linearGradient id="sky" x1="0" y1="0" x2="1" y2="0.3">
          <stop offset="0" stop-color="#3fd9f5"/>
          <stop offset="0.45" stop-color="#a9f6ff"/>
          <stop offset="0.75" stop-color="#33cdf3"/>
          <stop offset="1" stop-color="#1b7cf0"/>
        </linearGradient>
        <linearGradient id="swoosh" x1="0" y1="0" x2="1" y2="0">
          <stop offset="0" stop-color="#1b6ff0" stop-opacity="0.85"/>
          <stop offset="1" stop-color="#38c8f4" stop-opacity="0.2"/>
        </linearGradient>
      </defs>
      <rect width="1160" height="702" fill="url(#sky)"/>
      <path d="M0 0 H420 C250 60 120 150 0 220 Z" fill="#7fe6fb" opacity="0.55"/>
      <path d="M1160 0 C980 120 900 320 900 470 C900 580 960 660 1010 702 H1160 Z" fill="url(#swoosh)" opacity="0.6"/>
      <path d="M1080 0 C930 150 880 350 920 520 C945 610 990 670 1030 702" fill="none" stroke="#8feeff" stroke-width="14" opacity="0.45"/>
      <path d="M1160 20 C1040 150 1000 300 1010 470 C1020 580 1060 650 1100 702" fill="none" stroke="#8feeff" stroke-width="10" opacity="0.4"/>
      <path d="M0 480 C60 560 110 640 150 702 H0 Z" fill="#1c8cf0" opacity="0.35"/>
      <path d="M40 0 C-20 200 40 420 160 702" fill="none" stroke="#b9f7ff" stroke-width="12" opacity="0.35"/>
    </svg>

    <div class="brand-mark" role="img" aria-label="Coastal Pipeguard Services company mark"></div>

    <h1 class="company-name">
      <span>Coastal</span>
      <span>Pipeguard</span>
      <span>Services</span>
      <span>P/L</span>
    </h1>

    <p class="motto">"Protecting Australia's Underground Utilities"</p>

    <ul class="services">
      <li class="services__item">
        <svg class="services__star" viewBox="0 0 24 24" aria-hidden="true"><path d="M12 1.5l3.1 7.1 7.7.7-5.8 5.1 1.7 7.6L12 18l-6.7 4 1.7-7.6-5.8-5.1 7.7-.7z"/></svg>
        Vacuum Excavation &amp; Utility Location
      </li>
      <li class="services__item">
        <svg class="services__star" viewBox="0 0 24 24" aria-hidden="true"><path d="M12 1.5l3.1 7.1 7.7.7-5.8 5.1 1.7 7.6L12 18l-6.7 4 1.7-7.6-5.8-5.1 7.7-.7z"/></svg>
        Wet &amp; Dry Vacuum Loading
      </li>
      <li class="services__item">
        <svg class="services__star" viewBox="0 0 24 24" aria-hidden="true"><path d="M12 1.5l3.1 7.1 7.7.7-5.8 5.1 1.7 7.6L12 18l-6.7 4 1.7-7.6-5.8-5.1 7.7-.7z"/></svg>
        Confined Space Entry Specialists
      </li>
      <li class="services__item">
        <svg class="services__star" viewBox="0 0 24 24" aria-hidden="true"><path d="M12 1.5l3.1 7.1 7.7.7-5.8 5.1 1.7 7.6L12 18l-6.7 4 1.7-7.6-5.8-5.1 7.7-.7z"/></svg>
        High Pressure Cleaning
      </li>
    </ul>

    <div class="contact contact--email">
      <svg class="contact__icon" viewBox="0 0 52 52" aria-hidden="true">
        <rect x="1" y="1" width="50" height="50" rx="9" fill="var(--icon-blue)" stroke="#bdf3ff" stroke-width="2"/>
        <rect x="6" y="5" width="40" height="18" rx="6" fill="#ffffff" opacity="0.25"/>
        <text x="26" y="34" text-anchor="middle" font-size="24" fill="#ffffff" font-family="Arial, sans-serif">@</text>
      </svg>
      <span>coreyh@pipeguardco.com.au</span>
    </div>

    <div class="contact contact--phone">
      <svg class="contact__icon" viewBox="0 0 52 52" aria-hidden="true">
        <rect x="1" y="1" width="50" height="50" rx="9" fill="var(--icon-blue)" stroke="#bdf3ff" stroke-width="2"/>
        <rect x="6" y="5" width="40" height="18" rx="6" fill="#ffffff" opacity="0.25"/>
        <path d="M17 13c2-1 3.5-.5 4.5 1.5l2 4c.6 1.3.2 2.5-1 3.3l-1.5 1c1.2 3 3.5 5.5 6.5 7l1.1-1.4c.9-1.1 2.1-1.4 3.4-.8l4 2c1.9 1 2.3 2.5 1.3 4.4-1.6 3-4.3 4-7.5 3C20 34 14 27 13 20c-.4-3 1.2-5.7 4-7z" fill="#ffffff"/>
      </svg>
      <span>0413862975</span>
    </div>
  </div>
</div>
</body>
</html>
```